design an extra page for our profile

we are looking for someone to create another page like the attached but with the below changes:
heading changed to (Construction)
icons changed and names to reflect new services i.e
- Residential Building
- Commercial Building
- Landscaping
- Concrete
- Painting

the very bottom of the page is to stay the same with our office info

```html
<!DOCTYPE html>
<html lang="en">
<head>
<meta charset="utf-8">
<title>Construction Services</title>
<link rel="stylesheet" href="https://fonts.googleapis.com/css2?family=Montserrat:wght@400;700&family=Nunito+Sans:wght@400&family=Roboto:wght@400;500;700&display=swap">
<style>
  :root {
    --brand-blue: #1d2ff2;
    --white: #ffffff;
    --rule: rgba(255,255,255,0.75);
    --tone-top: #3a2a3c;
    --tone-mid: #6b3848;
    --tone-bottom: #241a24;
  }
  html, body { margin: 0; padding: 0; overflow: hidden; background: #ffffff; }
  .page {
    position: relative;
    width: 926px;
    height: 1200px;
    overflow: hidden;
    background: var(--brand-blue);
    color: var(--white);
  }
  .intro {
    position: absolute; left: 0; top: 0; width: 926px; height: 309px;
    background: var(--brand-blue);
  }
  .intro-title {
    position: absolute; left: 0; top: 48px; width: 926px; margin: 0;
    text-align: center;
    font-family: "Montserrat", sans-serif;
    font-size: 41px; font-weight: 400; letter-spacing: 0.5px; line-height: 1;
  }
  .intro-title strong { font-weight: 700; }
  .intro-rule {
    position: absolute; left: 79px; top: 124px; width: 768px; height: 1px;
    background: var(--rule);
  }
  .intro-offer {
    position: absolute; left: 60px; top: 149px; width: 806px; margin: 0;
    text-align: center;
    font-family: "Nunito Sans", sans-serif;
    font-size: 28.5px; line-height: 43px;
  }
  .services {
    position: absolute; left: 0; top: 309px; width: 926px; height: 738px;
  }
  .services-photo {
    position: absolute; inset: 0;
    background: linear-gradient(180deg, var(--tone-top) 0%, var(--tone-mid) 55%, var(--tone-bottom) 100%);
  }
  .service {
    position: absolute; width: 260px; text-align: center;
    font-family: "Roboto", sans-serif; font-weight: 500;
    font-size: 26px; line-height: 36px;
  }
  .service-icon { display: block; margin: 0 auto 12px; }
  .service--residential { left: 180px; top: 57px; }
  .service--commercial  { left: 471px; top: 57px; }
  .service--landscaping { left: 60px;  top: 261px; }
  .service--painting    { left: 347px; top: 261px; }
  .service--concrete    { left: 610px; top: 261px; }
  .service--residential .service-icon,
  .service--commercial .service-icon { margin-bottom: 14px; }
  .contact {
    position: absolute; left: 0; top: 1047px; width: 926px; height: 153px;
    background: var(--brand-blue);
    font-family: "Roboto", sans-serif; font-size: 18.5px;
  }
  .contact-brand {
    position: absolute; left: 30px; top: 55px; width: 146px;
    text-align: center;
    font-family: "Roboto", sans-serif; font-weight: 700; font-size: 34px; line-height: 40px;
  }
  .contact-office { position: absolute; left: 207px; top: 42px; margin: 0; white-space: nowrap; }
  .contact-rule {
    position: absolute; left: 207px; top: 74px; width: 686px; height: 1px;
    background: var(--rule);
  }
  .contact-web { position: absolute; left: 207px; top: 91px; margin: 0; white-space: nowrap; }
  .contact strong { font-weight: 700; }
  .contact .sep { display: inline-block; width: 1px; height: 20px; background: var(--white); vertical-align: -4px; margin: 0 5px; }
</style>
</head>
<body>
<main class="page">
  <header class="intro">
    <h1 class="intro-title"><strong>CONSTRUCTION</strong> SERVICES</h1>
    <div class="intro-rule"></div>
    <p class="intro-offer">As new tenants to buiding and as a way of<br>introducing ourselves we would like to offer a<br>10% discount on any of the below services.</p>
  </header>

  <section class="services">
    <div class="services-photo" role="img" aria-label="Photo of a construction site in silhouette at sunset"></div>

    <div class="service service--residential">
      <svg class="service-icon" width="78" height="78" viewBox="0 0 78 78" fill="none" stroke="#fff" stroke-width="2">
        <circle cx="39" cy="39" r="37"/>
        <path d="M22 30 L39 20 L56 30 Z"/>
        <rect x="24" y="30" width="30" height="28"/>
        <rect x="29" y="35" width="6" height="6"/><rect x="43" y="35" width="6" height="6"/>
        <rect x="35" y="46" width="8" height="12"/>
      </svg>
      Residential<br>Building
    </div>

    <div class="service service--commercial">
      <svg class="service-icon" width="78" height="78" viewBox="0 0 78 78" fill="none" stroke="#fff" stroke-width="2">
        <circle cx="39" cy="39" r="37"/>
        <path d="M44 16 L44 60 M50 16 L50 60 M44 24 L50 24 M44 34 L50 34 M44 44 L50 44"/>
        <path d="M20 22 L60 22 L60 26 L20 26 Z"/>
        <path d="M25 26 L25 36"/>
        <circle cx="25" cy="40" r="4"/>
        <path d="M40 60 L54 60"/>
      </svg>
      Commercial<br>Building
    </div>

    <div class="service service--landscaping">
      <svg class="service-icon" width="78" height="78" viewBox="0 0 78 78" fill="none" stroke="#fff" stroke-width="2">
        <circle cx="39" cy="39" r="37"/>
        <rect x="20" y="30" width="38" height="18"/>
        <path d="M20 36 L58 36 M20 42 L58 42 M30 30 L30 36 M44 30 L44 36 M25 36 L25 42 M37 36 L37 42 M51 36 L51 42 M30 42 L30 48 M44 42 L44 48"/>
      </svg>
      Landscaping
    </div>

    <div class="service service--painting">
      <svg class="service-icon" width="78" height="78" viewBox="0 0 78 78" fill="none" stroke="#fff" stroke-width="2">
        <circle cx="39" cy="39" r="37"/>
        <path d="M27 30 C27 18 51 18 51 30"/>
        <path d="M25 30 L53 30 L50 58 L28 58 Z"/>
        <path d="M26 38 L52 38 M34 38 L34 46 M42 38 L42 50"/>
      </svg>
      Painting
    </div>

    <div class="service service--concrete">
      <svg class="service-icon" width="78" height="78" viewBox="0 0 78 78" fill="none" stroke="#fff" stroke-width="2">
        <circle cx="39" cy="39" r="37"/>
        <path d="M22 34 L52 34 L46 46 L28 46 Z"/>
        <path d="M28 34 C28 24 44 24 46 34"/>
        <path d="M46 46 L58 40"/>
        <circle cx="30" cy="52" r="5"/>
        <path d="M28 46 L24 56 M44 46 L48 56"/>
      </svg>
      Concrete
    </div>
  </section>

  <footer class="contact">
    <div class="contact-brand">KORVA</div>
    <p class="contact-office"><strong>HOME office:</strong> 1300 42 7816&nbsp;&nbsp;&nbsp;Suit 4.02, 12 Parkline Drive Glen Ridge</p>
    <div class="contact-rule"></div>
    <p class="contact-web"><strong>WWW.KORVA-SERVICES.com.AU</strong> Sydney<span class="sep"></span>Canberra<span class="sep"></span>Brisbane<span class="sep"></span>Melbourne</p>
  </footer>
</main>
</body>
</html>
```